Company Gift Card Designs

I would like to have 2 gift cards designed.

Both cards need to be in our company colors and have a non-white background. Both will need to follow the attached spec sheet from the card vendor.

Card 1 - will need to have the words Thank you on the card and use the KTB Logo

Card 2 - will need to have both the KTB logo and the Zel480 Logo incorporated into the design.

```html
<!DOCTYPE html>
<html lang="en">
<head>
<meta charset="utf-8">
<title>Thank You Gift Cards</title>
<link rel="stylesheet" href="https://fonts.googleapis.com/css2?family=Playfair+Display:wght@900&display=swap">
<style>
  :root {
    --page: #ffffff;
    --red: #c41c24;
    --red-light: #d8222b;
    --red-deep: #9e151c;
    --shadow-red: #7a0f14;
    --white: #ffffff;
    --grey-lower: #dcdcdc;
    --ink: #2e2e2e;
    --pink: #f6a0a8;
    --pink-soft: #fbd9dc;
  }
  * { box-sizing: border-box; margin: 0; padding: 0; }
  html, body {
    width: 800px;
    height: 1200px;
    overflow: hidden;
    background: var(--page);
  }
  .sheet {
    position: relative;
    width: 800px;
    height: 1200px;
  }
  .gift-card {
    position: absolute;
    left: 80px;
    width: 640px;
    height: 410px;
    overflow: hidden;
    background: radial-gradient(ellipse at 55% 50%, var(--red-light) 0%, var(--red) 45%, var(--red-deep) 100%);
    box-shadow: 0 4px 6px rgba(0,0,0,0.35);
  }
  .gift-card--dual { top: 150px; }
  .gift-card--single { top: 640px; }

  .frame-line {
    position: absolute;
    border: 1px solid rgba(255,255,255,0.85);
  }
  .frame-line--outer { inset: 27px 28px; }
  .frame-line--inner { inset: 44px 44px; border-color: rgba(255,255,255,0.35); }

  .corner-flourish {
    position: absolute;
    width: 90px;
    height: 150px;
    background: radial-gradient(ellipse 50% 50% at 50% 50%, rgba(255,255,255,0.42) 0%, rgba(255,255,255,0.18) 55%, rgba(255,255,255,0) 100%);
  }
  .corner-flourish--top-right { top: 14px; right: 10px; }
  .corner-flourish--bottom-left { bottom: 14px; left: 10px; }

  .logo-tab {
    position: absolute;
    top: 0;
    left: 50%;
    width: 196px;
    height: 146px;
    transform: translateX(-50%);
    background: var(--white);
    border-radius: 0 0 98px 98px;
    box-shadow: 0 0 0 5px var(--red), 0 0 0 7px rgba(255,255,255,0.9);
    display: flex;
    flex-direction: column;
    align-items: center;
    justify-content: flex-start;
    gap: 6px;
  }
  .gift-card--dual .logo-tab { padding-top: 26px; }
  .gift-card--single .logo-tab { padding-top: 42px; }
  .logo-tab::after {
    content: "";
    position: absolute;
    inset: -2px 6px 6px 6px;
    border: 2px solid var(--red);
    border-top: none;
    border-radius: 0 0 92px 92px;
  }
  .brand-name {
    font-family: "Playfair Display", Georgia, serif;
    font-weight: 900;
    color: var(--ink);
    line-height: 1;
    display: flex;
    align-items: center;
    gap: 8px;
  }
  .brand-name--primary { font-size: 40px; }
  .brand-name--partner { font-size: 34px; }
  .brand-mark {
    width: 12px;
    height: 12px;
    border-radius: 50%;
    background: var(--red);
  }

  .greeting {
    position: absolute;
    left: 0;
    right: 0;
    text-align: center;
  }
  .gift-card--dual .greeting { top: 178px; }
  .gift-card--single .greeting { top: 166px; }
  .splash-ornament {
    position: absolute;
    left: 50%;
    top: -40px;
    width: 380px;
    height: 260px;
    transform: translateX(-50%);
    background: radial-gradient(ellipse 50% 50% at 50% 50%, rgba(246,160,168,0.35) 0%, rgba(246,160,168,0.18) 55%, rgba(246,160,168,0) 100%);
  }
  .greeting-text {
    position: relative;
    font-family: "Playfair Display", Georgia, serif;
    font-weight: 900;
    font-size: 86px;
    line-height: 0.92;
    letter-spacing: -1px;
  }
  .greeting-line {
    display: block;
    background: linear-gradient(to bottom, var(--white) 0%, var(--white) 62%, var(--grey-lower) 62%, var(--grey-lower) 100%);
    -webkit-background-clip: text;
    background-clip: text;
    color: transparent;
    filter: drop-shadow(3px 3px 0 var(--shadow-red));
  }
</style>
</head>
<body>
<main class="sheet">

  <section class="gift-card gift-card--dual" aria-label="Gift card with KTB and Zel480">
    <div class="frame-line frame-line--outer"></div>
    <div class="frame-line frame-line--inner"></div>
    <div class="corner-flourish corner-flourish--top-right" role="img" aria-label="White scroll flourish ornament"></div>
    <div class="corner-flourish corner-flourish--bottom-left" role="img" aria-label="White scroll flourish ornament"></div>
    <div class="logo-tab">
      <span class="brand-name brand-name--primary">KTB</span>
      <span class="brand-name brand-name--partner">Zel480</span>
    </div>
    <div class="greeting">
      <div class="splash-ornament" role="img" aria-label="Pink and white splash ornaments with sparkles"></div>
      <h2 class="greeting-text">
        <span class="greeting-line">Thank</span>
        <span class="greeting-line">You</span>
      </h2>
    </div>
  </section>

  <section class="gift-card gift-card--single" aria-label="Gift card with KTB">
    <div class="frame-line frame-line--outer"></div>
    <div class="frame-line frame-line--inner"></div>
    <div class="corner-flourish corner-flourish--top-right" role="img" aria-label="White scroll flourish ornament"></div>
    <div class="corner-flourish corner-flourish--bottom-left" role="img" aria-label="White scroll flourish ornament"></div>
    <div class="logo-tab">
      <span class="brand-name brand-name--primary"><span class="brand-mark"></span>KTB</span>
    </div>
    <div class="greeting">
      <div class="splash-ornament" role="img" aria-label="Pink and white splash ornaments with sparkles"></div>
      <h2 class="greeting-text">
        <span class="greeting-line">Thank</span>
        <span class="greeting-line">You</span>
      </h2>
    </div>
  </section>

</main>
</body>
</html>
```